A4 sized 'product advertisement'

Require a A4 Sized advertisement to promote a new product.

File must be provided in .psd format, unflattened, unmerged as the specifics of the item advertised will be decided at a later date.

Add must include:
- logo
- business name, address, phone number, website and email address
- area for product name
- area for product dimension
- area for product cost
- area for product photo
- document be suitable with the correct 'bleed' for printing
- include a border

I have attached Logo in .psd format.
Design can be in website contrast - or can be completely different. (will consider new 'exciting' ideas)
Updates

TEMPLATE IS NOT TO USE PICTURES FROM THE WEBSITE - AND IS ONLY TO PROMOTE ONE ITEM NOT MULTIPLE.

Industry/Entity Type

Trade

Requirements
Must have
• - be simple, yet eye catching.
• - easy to read.

```html
<!DOCTYPE html>
<html lang="en">
<head>
<meta charset="utf-8">
<title>Barrow Timber – Redgum Posts</title>
<link rel="stylesheet" href="https://fonts.googleapis.com/css2?family=Open+Sans:wght@400;600;700&display=swap">
<style>
  :root {
    --navy: #0f3468;
    --navy-deep: #0a2550;
    --navy-bright: #14468c;
    --paper: #f3f3f3;
    --ink: #222222;
    --white: #ffffff;
    --tick: #7cc242;
    --ring: #b9bcc0;
    --wood-light: #d9977a;
    --wood-dark: #8a4e34;
  }
  * { margin: 0; padding: 0; box-sizing: border-box; }
  html, body { width: 987px; height: 1200px; overflow: hidden; background: var(--paper); }
  body { font-family: "Open Sans", Arial, sans-serif; color: var(--ink); }
  .flyer { position: relative; width: 987px; height: 1200px; overflow: hidden; background: var(--paper); }
  .backdrop { position: absolute; inset: 0; }

  .product-photo { position: absolute; left: 0; top: 0; width: 987px; height: 600px; }

  .price-panel {
    position: absolute; left: 551px; top: 560px; width: 399px; height: 429px;
    background: linear-gradient(180deg, var(--navy-bright) 0%, var(--navy) 45%, var(--navy-deep) 100%);
    border-radius: 0 0 18px 18px; color: var(--white);
  }
  .price-panel h2 {
    position: absolute; left: 50px; top: 138px; font-size: 30px; font-weight: 700; letter-spacing: 0.3px;
  }
  .price-list { position: absolute; left: 20px; top: 200px; width: 362px; list-style: none; }
  .price-list li {
    display: flex; align-items: baseline; height: 45.5px; font-size: 24px; letter-spacing: 0.5px;
  }
  .price-list .size { font-weight: 400; }
  .price-list .leader { flex: 1; border-bottom: 2px dotted var(--white); margin: 0 2px 6px; opacity: .9; }
  .price-list .cost { font-weight: 700; font-size: 25px; }

  .inset-photo {
    position: absolute; left: 686px; top: 382px; width: 272px; height: 272px; border-radius: 50%;
    background: linear-gradient(160deg, #ffffff, #9ea2a7);
    box-shadow: 0 4px 10px rgba(0,0,0,.35);
  }
  .inset-photo .inner {
    position: absolute; inset: 12px; border-radius: 50%;
    background: linear-gradient(180deg, #3f4750 0%, #3f4750 22%, #d8ccab 23%, #c7b993 68%, #a59a84 72%, #8f8676 100%);
  }

  .brand { position: absolute; left: 78px; top: 640px; display: flex; align-items: center; gap: 14px; }
  .brand .mark { width: 30px; height: 30px; background: var(--navy); }
  .brand .name { font-size: 42px; font-weight: 700; color: var(--navy); letter-spacing: 1px; }

  .intro { position: absolute; left: 36px; top: 760px; width: 470px; font-size: 19.5px; line-height: 21px; color: var(--ink); }

  .range { position: absolute; left: 36px; top: 870px; list-style: none; }
  .range li { display: flex; align-items: center; gap: 14px; height: 44px; font-size: 20px; }
  .range svg { width: 20px; height: 16px; }

  .footer { position: absolute; left: 0; top: 1090px; width: 987px; color: var(--white); }
  .call { display: flex; justify-content: center; align-items: center; gap: 18px; font-size: 27px; font-weight: 700; }
  .call svg { width: 26px; height: 26px; }
  .contacts {
    display: flex; justify-content: space-between; margin: 20px 20px 0 24px; font-size: 16.5px;
  }
  .contacts span { display: flex; align-items: center; gap: 12px; }
  .contacts svg { width: 24px; height: 24px; }
</style>
</head>
<body>
<main class="flyer">
  <div class="product-photo" role="img" aria-label="Photo of a strapped stack of sawn redgum timber posts on a forklift in a warehouse" style="background: linear-gradient(115deg, #7d7f82 0%, #6c6e70 18%, var(--wood-light) 32%, #c77e5f 55%, var(--wood-dark) 78%, #9a9a94 100%);"></div>

  <svg class="backdrop" width="987" height="1200" viewBox="0 0 987 1200" aria-hidden="true">
    <defs>
      <linearGradient id="navyFade" x1="0" y1="0" x2="0" y2="1">
        <stop offset="0" stop-color="#14468c"/>
        <stop offset="1" stop-color="#0a2550"/>
      </linearGradient>
    </defs>
    <path d="M0 455 Q420 640 987 440 L987 520 Q430 640 0 520 Z" fill="url(#navyFade)"/>
    <path d="M0 500 Q440 660 987 485 L987 1200 L0 1200 Z" fill="var(--paper)"/>
    <path d="M0 480 Q430 640 987 470" fill="none" stroke="#ffffff" stroke-width="6"/>
    <path d="M0 1010 Q494 1080 987 1010 L987 1200 L0 1200 Z" fill="#c9cbce"/>
    <path d="M0 1025 Q494 1095 987 1025 L987 1200 L0 1200 Z" fill="var(--white)"/>
    <path d="M0 1035 Q494 1105 987 1035 L987 1200 L0 1200 Z" fill="url(#navyFade)"/>
  </svg>

  <section class="price-panel">
    <h2>REDGUM POSTS</h2>
    <ul class="price-list">
      <li><span class="size">100x100x2100</span><span class="leader"></span><span class="cost">$31.00</span></li>
      <li><span class="size">100x100x2400</span><span class="leader"></span><span class="cost">$35.00</span></li>
      <li><span class="size">125x75x2400</span><span class="leader"></span><span class="cost">$28.70</span></li>
      <li><span class="size">125x75x2700</span><span class="leader"></span><span class="cost">$31.20</span></li>
    </ul>
  </section>

  <div class="inset-photo">
    <div class="inner" role="img" aria-label="Photo of a finished timber paling fence in front of a building"></div>
  </div>

  <div class="brand">
    <span class="mark"></span>
    <span class="name">BARROW TIMBER</span>
  </div>

  <p class="intro">Our wide range of products will ensure that you will be able to construct your fence quick, easy and hasle free.&nbsp; We are also able to assist in the installation service of Timber Fences.</p>

  <ul class="range">
    <li><svg viewBox="0 0 20 16"><path d="M2 8 L8 14 L18 2" fill="none" stroke="var(--tick)" stroke-width="3"/></svg>Redgum Posts</li>
    <li><svg viewBox="0 0 20 16"><path d="M2 8 L8 14 L18 2" fill="none" stroke="var(--tick)" stroke-width="3"/></svg>Redgum Sleepers</li>
    <li><svg viewBox="0 0 20 16"><path d="M2 8 L8 14 L18 2" fill="none" stroke="var(--tick)" stroke-width="3"/></svg>Custom Orders</li>
  </ul>

  <footer class="footer">
    <div class="call">
      <span>Give us a call at</span>
      <span style="display:flex;align-items:center;gap:12px;">
        <svg viewBox="0 0 24 24"><path d="M6.6 10.8c1.4 2.8 3.8 5.1 6.6 6.6l2.2-2.2c.3-.3.7-.4 1-.2 1.1.4 2.3.6 3.6.6.6 0 1 .4 1 1V20c0 .6-.4 1-1 1C10.6 21 3 13.4 3 4c0-.6.4-1 1-1h3.5c.6 0 1 .4 1 1 0 1.3.2 2.5.6 3.6.1.3 0 .7-.2 1l-2.3 2.2z" fill="var(--white)"/></svg>
        (03) 9000-4812
      </span>
    </div>
    <div class="contacts">
      <span><svg viewBox="0 0 24 24"><circle cx="12" cy="12" r="11" fill="none" stroke="var(--white)" stroke-width="1.5"/><path d="M12 5.5c-2.5 0-4.3 1.9-4.3 4.2 0 3.2 4.3 8 4.3 8s4.3-4.8 4.3-8c0-2.3-1.8-4.2-4.3-4.2zm0 5.9a1.7 1.7 0 110-3.4 1.7 1.7 0 010 3.4z" fill="var(--white)"/></svg>12 Ironbark Road, Millbrook VIC 3999</span>
      <span><svg viewBox="0 0 24 24"><circle cx="12" cy="12" r="11" fill="none" stroke="var(--white)" stroke-width="1.5"/><rect x="6" y="8" width="12" height="8.5" rx="1" fill="none" stroke="var(--white)" stroke-width="1.5"/><path d="M6.5 8.5 L12 13 L17.5 8.5" fill="none" stroke="var(--white)" stroke-width="1.5"/></svg>info@barrowtimber.com</span>
      <span><svg viewBox="0 0 24 24"><circle cx="12" cy="12" r="11" fill="none" stroke="var(--white)" stroke-width="1.5"/><circle cx="12" cy="12" r="6.5" fill="none" stroke="var(--white)" stroke-width="1.2"/><ellipse cx="12" cy="12" rx="3" ry="6.5" fill="none" stroke="var(--white)" stroke-width="1.2"/><path d="M5.5 12h13M6.5 9h11M6.5 15h11" stroke="var(--white)" stroke-width="1"/></svg>barrowtimber.com.au</span>
    </div>
  </footer>
</main>
</body>
</html>
```